Refresh of Business Card Design

Want to refresh the business card design with the new logo while adhering to style guide as attached. Would like to match feel of website www.durmackvinex.com

```html
<!DOCTYPE html>
<html lang="en">
<head>
<meta charset="utf-8">
<title>Durmack Vinex — Business Card</title>
<link rel="stylesheet" href="https://fonts.googleapis.com/css2?family=Poppins:wght@700&family=Work+Sans:wght@400;500&display=swap">
<style>
  :root {
    --backdrop: #c3cfe0;
    --card-black: #070707;
    --card-light: #eef1f6;
    --brand-red: #e21b3c;
    --accent-red: #c8102e;
    --ink: #1b1b1b;
    --white: #ffffff;
  }
  * { margin: 0; padding: 0; box-sizing: border-box; }
  html, body {
    width: 900px; height: 1200px; overflow: hidden;
    background: var(--backdrop);
    font-family: "Work Sans", sans-serif;
  }
  .canvas { position: relative; width: 900px; height: 1200px; }
  .card {
    position: absolute; width: 631px; height: 358px; overflow: hidden;
    background: var(--card-black);
  }
  .card--front { left: 134px; top: 214px; }
  .card--back { left: 135px; top: 628px; }

  .brand {
    position: absolute; display: flex; align-items: center; gap: 12px;
    transform: translate(-50%, -50%);
    color: var(--white); font-weight: 400; letter-spacing: 1px; white-space: nowrap;
  }
  .brand__dot { border-radius: 50%; background: var(--brand-red); flex: none; }
  .card--front .brand { left: 315px; top: 182px; font-size: 30px; }
  .card--front .brand__dot { width: 26px; height: 26px; }
  .card--back .brand { left: 160px; top: 182px; font-size: 22px; }
  .card--back .brand__dot { width: 18px; height: 18px; }

  .card__panel { position: absolute; inset: 0; }

  .contact { position: absolute; left: 373px; top: 0; color: var(--ink); }
  .contact__name {
    position: absolute; top: 56px; left: 0; white-space: nowrap;
    font-family: "Poppins", sans-serif; font-weight: 700; font-size: 22.5px;
    color: var(--brand-red); letter-spacing: 0.6px;
  }
  .contact__line {
    position: absolute; left: 0; white-space: nowrap;
    font-size: 14px; letter-spacing: 0.9px; line-height: 18px;
  }
  .contact__item {
    position: absolute; left: 0; display: flex; align-items: center; gap: 10px;
    white-space: nowrap; font-size: 14px; letter-spacing: 0.9px; line-height: 18px;
  }
  .contact__icon { width: 16px; height: 16px; flex: none; }
</style>
</head>
<body>
<div class="canvas">

  <section class="card card--front">
    <div class="brand"><span class="brand__dot"></span><span>DURMACK VINEX</span></div>
  </section>

  <section class="card card--back">
    <div class="brand"><span class="brand__dot"></span><span>DURMACK VINEX</span></div>

    <svg class="card__panel" viewBox="0 0 631 358" width="631" height="358">
      <path fill="var(--accent-red)" d="M311,0 L319,0 C330,80 345,140 343,200 C342,260 335,320 326,358 L316,358 C328,320 336,260 337,205 C338,140 322,80 311,0 Z"/>
      <path fill="var(--card-light)" d="M319,0 C330,80 345,140 343,200 C342,260 335,320 326,358 L631,358 L631,0 Z"/>
    </svg>

    <div class="contact">
      <div class="contact__name">REID CALLOWAY</div>
      <div class="contact__line" style="top:87px">Sales</div>
      <div class="contact__line" style="top:120px">274 Cedar Ridge Rd Borger,</div>
      <div class="contact__line" style="top:146px">Texas 79007</div>
      <div class="contact__line" style="top:176px">PO Box 48213 Midland,</div>
      <div class="contact__line" style="top:202px">Texas 79702</div>

      <div class="contact__item" style="top:237px">
        <svg class="contact__icon" viewBox="0 0 16 16"><path fill="var(--accent-red)" d="M3.5 1.5l2.6 2.8-1.4 1.8c.9 1.9 2.3 3.3 4.2 4.2l1.8-1.4 2.8 2.6-1.6 2.3C6.6 13.7 2.3 9.4 1.2 3.1z"/><path fill="none" stroke="var(--accent-red)" stroke-width="1.3" d="M9.5 4a3 3 0 0 1 2.5 2.5M9.8 1.4a5.5 5.5 0 0 1 4.8 4.8"/></svg>
        <span>806.555.0142</span>
      </div>
      <div class="contact__item" style="top:262px">
        <svg class="contact__icon" viewBox="0 0 16 16"><rect x="1" y="3" width="14" height="10" fill="var(--accent-red)"/><path fill="none" stroke="var(--card-light)" stroke-width="1.3" d="M1.5 3.8L8 8.8l6.5-5"/></svg>
        <span>rcalloway@durmackvinex.com</span>
      </div>
      <div class="contact__item" style="top:287px">
        <svg class="contact__icon" viewBox="0 0 16 16"><g fill="none" stroke="var(--accent-red)" stroke-width="1.4"><circle cx="8" cy="8" r="6.5"/><ellipse cx="8" cy="8" rx="2.8" ry="6.5"/><path d="M1.5 8h13M2.5 4.8h11M2.5 11.2h11"/></g></svg>
        <span>www.durmackvinex.com</span>
      </div>
    </div>
  </section>

</div>
</body>
</html>
```